Health - Still Meadow Project

I am running a new Still Meadow Conference that will have meditation, mediums and healers - this is a first time conference. However the conference is aimed at mainstream 'normal' people. The 'normal' people, don't want to hear or see words like Tantra, Prana, Angels, etc, but they have problems that can be alleviated through these mediums. The design should communicate light, soothing, comforting, healing. I would like a web design for a single page that can be used as a landing page for the conference registration. I also need a logo and a flyer that can be made into posters A4 or A3 posters. I need to be able to edit all documents as there will be changes in the program through time. I have attached the initial agenda. This conference will be held in Victoria, Australia.
Target Market(s)
Mums and grandmas
Industry/Entity Type
Health And Wellness
Number of Pages Required
1 page

```html
<!DOCTYPE html>
<html lang="en">
<head>
<meta charset="utf-8">
<title>Still Meadow Conference</title>
<link href="https://fonts.googleapis.com/css2?family=Roboto:wght@400;500;700;900&family=Open+Sans:wght@400;600&display=swap" rel="stylesheet">
<style>
:root{
  --teal:#1bb3ae;
  --teal-light:#22cdc3;
  --teal-dark:#14a3a3;
  --lime:#bdd12a;
  --lime-light:#d3e04a;
  --ink:#333333;
  --muted:#555555;
  --paper:#ffffff;
  --mist:#f2f2f2;
  --footer:#333333;
  --footer-deep:#262626;
  --footer-text:#cfcfcf;
}
*{margin:0;padding:0;box-sizing:border-box}
html,body{width:1200px;height:3220px;overflow:hidden}
body{position:relative;background:var(--paper);font-family:'Open Sans',sans-serif;color:var(--ink)}
.abs{position:absolute}
.heading{font-family:'Roboto',sans-serif;font-weight:700;text-transform:uppercase}

/* header */
.site-header{left:0;top:0;width:1200px;height:140px;background:var(--paper);border-top:5px solid var(--teal)}
.brand{left:130px;top:22px;display:flex;align-items:center;gap:14px}
.brand-dot{width:34px;height:34px;border-radius:50%;background:var(--teal)}
.brand-name{font-family:'Roboto',sans-serif;font-weight:700;font-size:30px;line-height:34px;color:var(--teal);text-transform:uppercase;width:170px}
.main-nav{left:568px;top:62px;display:flex;gap:34px;font-family:'Roboto',sans-serif;font-weight:700;font-size:12.5px;text-transform:uppercase;color:var(--ink)}
.main-nav .active{color:var(--teal)}

/* hero */
.hero{left:0;top:140px;width:1200px;height:408px;background:linear-gradient(100deg,#5fd0c8 0%,#8fe0d6 45%,#d9eee4 65%,#9fd8cf 100%)}
.hero-title{left:130px;top:222px;font-size:46px;font-weight:900;color:var(--paper);letter-spacing:1px}
.hero-text{left:130px;top:305px;width:390px;font-size:11.5px;line-height:20px;color:var(--paper)}
.btn{display:inline-block;background:var(--teal);color:var(--paper);font-family:'Roboto',sans-serif;font-weight:700;font-size:11.5px;text-transform:uppercase;text-align:center;border-radius:3px}
.hero-btn{left:130px;top:370px;width:145px;height:45px;line-height:45px;background:var(--teal-dark)}
.dots{display:flex;gap:10px}
.dots span{width:14px;height:14px;border-radius:50%;border:2px solid var(--paper);background:rgba(255,255,255,.4)}
.dots .on{background:var(--teal)}
.hero-dots{left:133px;top:453px}

/* newsletter band */
.news-band{left:0;top:548px;width:1200px;height:88px;background:linear-gradient(90deg,var(--lime) 0%,var(--lime-light) 60%,#c4d63a 100%)}
.band-title{left:130px;top:560px;font-size:27px;color:var(--paper)}
.band-sub{left:130px;top:597px;font-size:9.5px;color:var(--paper);text-transform:uppercase}
.band-input{left:623px;top:569px;width:307px;height:45px;background:var(--paper);border-radius:2px;display:flex;align-items:center;padding-left:18px;gap:12px;font-size:11px;color:#666}
.band-btn{left:945px;top:569px;width:122px;height:45px;line-height:45px}

/* welcome */
.welcome-kicker{left:133px;top:706px;font-size:24px;color:var(--ink)}
.welcome-title{left:133px;top:734px;font-size:35px;color:var(--teal)}
.welcome-title em{font-style:normal;color:var(--lime)}
.welcome-text{left:133px;top:784px;width:430px;font-size:11.5px;line-height:22px;color:var(--muted);text-align:justify}
.welcome-btn{left:133px;top:923px;width:116px;height:44px;line-height:44px}
.video{left:616px;top:706px;width:447px;height:249px;background:linear-gradient(180deg,#dfe6ef 0%,#9aa6b7 45%,#4a4a55 100%)}
.video-bar{left:616px;top:920px;width:447px;height:35px;background:rgba(0,0,0,.75)}

/* solutions */
.solutions{left:0;top:1046px;width:1200px;height:504px;background:linear-gradient(180deg,var(--teal-light) 0%,var(--teal-dark) 100%)}
.section-title{width:1200px;left:0;text-align:center;font-size:29px}
.solutions-title{top:1080px;color:var(--paper)}
.solution{top:1170px;width:300px;text-align:center;color:var(--paper)}
.solution-icon{width:128px;height:128px;border-radius:50%;background:var(--lime);margin:0 auto;display:flex;align-items:center;justify-content:center}
.solution h3{font-size:20px;margin-top:30px}
.solution p{font-size:11.5px;line-height:22px;margin-top:14px;padding:0 12px}
.solution .more{display:block;margin-top:18px;font-size:10.5px;text-decoration:underline;text-transform:uppercase}

/* testimonial */
.testimonial{left:0;top:1550px;width:1200px;height:333px;background:linear-gradient(180deg,#0c1a2e 0%,#16263e 55%,#3a2a28 100%)}
.avatar-big{left:542px;top:1589px;width:116px;height:116px;border-radius:50%;border:4px solid var(--paper);background:linear-gradient(135deg,#7fa15a,#c9b58a)}
.quote{left:150px;top:1744px;width:900px;text-align:center;font-size:12px;line-height:21px;color:var(--paper);font-style:italic}
.quote-name{left:0;top:1802px;width:1200px;text-align:center;font-size:12px;color:var(--lime)}
.quote-dots{left:571px;top:1836px}

/* speakers */
.speakers-title{top:1940px;color:var(--teal)}
.section-title em{font-style:normal;color:var(--lime)}
.speaker{top:2018px;width:214px;height:318px;background:#f4f4f4;box-shadow:0 3px 8px rgba(0,0,0,.18);text-align:center}
.speaker-photo{width:100px;height:100px;border-radius:50%;margin:30px auto 0;border:3px solid var(--paper)}
.speaker h3{font-size:18px;color:var(--teal);margin-top:34px}
.speaker p{font-size:11.5px;line-height:19px;color:var(--ink);margin-top:10px;padding:0 20px}
.speaker .more{display:block;margin-top:20px;font-size:10.5px;color:var(--teal);text-decoration:underline;text-transform:uppercase}

/* news */
.news{left:0;top:2396px;width:1200px;height:481px;background:var(--mist)}
.news-title{top:2449px;color:var(--teal)}
.post{top:2527px;width:286px}
.post-photo{height:150px;border:4px solid var(--paper);box-shadow:0 2px 6px rgba(0,0,0,.2)}
.post h3{font-size:17px;color:var(--teal);margin-top:30px}
.post time{display:block;font-size:11px;color:#777;margin-top:6px;text-transform:uppercase}
.post p{font-size:11.5px;line-height:20px;margin-top:12px}
.post .more{display:block;margin-top:16px;font-size:10.5px;color:var(--teal);text-decoration:underline;text-transform:uppercase}

/* footer */
.site-footer{left:0;top:2877px;width:1200px;height:275px;background:var(--footer)}
.foot-col{top:2922px;color:var(--footer-text)}
.foot-col h4{font-family:'Roboto',sans-serif;font-weight:700;font-size:17px;color:var(--paper);text-transform:uppercase;margin-bottom:22px}
.foot-links li{list-style:none;font-size:11.5px;line-height:16px}
.contact li{list-style:none;font-size:11.5px;line-height:18px;display:flex;gap:14px;margin-bottom:10px}
.contact svg{flex:none;margin-top:3px}
.foot-news p{font-size:11px}
.foot-input{width:196px;height:34px;background:#555;margin-top:18px;font-size:10.5px;color:#ddd;padding:10px 12px}
.foot-btn{width:84px;height:26px;line-height:26px;background:var(--lime);color:var(--paper);font-size:11px;margin-top:12px;text-align:center;border-radius:2px}
.foot-brand{left:865px;top:2926px;display:flex;align-items:center;gap:12px}
.foot-brand .brand-dot{background:#555}
.foot-brand .brand-name{color:#5a5a5a;font-size:24px;line-height:28px;width:140px}
.socials{left:912px;top:3010px;display:flex;gap:10px}
.socials span{width:34px;height:34px;border-radius:50%;border:2px solid var(--paper)}
.copyright{left:0;top:3152px;width:1200px;height:68px;background:var(--footer-deep);color:var(--footer-text);font-size:11px;text-align:center;line-height:68px}
</style>
</head>
<body>

<header class="abs site-header"></header>
<div class="abs brand"><span class="brand-dot"></span><span class="brand-name">Still Meadow</span></div>
<nav class="abs main-nav">
  <span class="active">Home</span><span>Our Solution</span><span>Why Choos us?</span><span>About Us</span><span>Blog</span><span>Contact Us</span>
</nav>

<section class="abs hero" role="img" aria-label="Photo of a woman meditating with eyes closed against a soft teal sky"></section>
<h1 class="abs heading hero-title">Meditation</h1>
<p class="abs hero-text">Lorem ipsum dolor sit amet, consectetur adipiscing elit, sed do eiusmod tempor incididunt ut labore et dolore magna aliqua.</p>
<span class="abs btn hero-btn">Book Appointment</span>
<div class="abs dots hero-dots"><span class="on"></span><span></span><span></span></div>

<section class="abs news-band"></section>
<h2 class="abs heading band-title">Subscribe Newsletter</h2>
<p class="abs band-sub">Subscribe newsletter to receive the latest news and updates direct to your inbox</p>
<div class="abs band-input">
  <svg width="14" height="11" viewBox="0 0 14 11"><rect x="0.5" y="0.5" width="13" height="10" fill="none" stroke="#555"/><path d="M0.5 0.5 L7 6 L13.5 0.5" fill="none" stroke="#555"/></svg>
  <span>Enter Your Mail Id</span>
</div>
<span class="abs btn band-btn">Subscribe</span>

<h2 class="abs heading welcome-kicker">Welcome to</h2>
<h2 class="abs heading welcome-title">Still <em>Meadow</em></h2>
<p class="abs welcome-text">Nemo enim ipsam voluptatem quia voluptas sit aspernatur aut odit aut fugit, sed quia consequuntur magni dolores eos qui ratione voluptatem sequi nesciunt. Neque porro quisquam est, qui dolorem ipsum quia dolor sit amet, consectetur, adipisci velit, sed quia non numquam eius modi tempora incidunt ut labore et dolore magnam aliquam quaerat voluptatem.</p>
<span class="abs btn welcome-btn">Read More</span>
<div class="abs video" role="img" aria-label="Video still of a speaker presenting to a full conference hall"></div>
<div class="abs video-bar">
  <svg width="447" height="35" viewBox="0 0 447 35">
    <path d="M14 11 L24 17.5 L14 24 Z" fill="#fff"/>
    <rect x="36" y="16" width="240" height="4" fill="#666"/>
    <rect x="36" y="16" width="90" height="4" fill="var(--teal)"/>
    <rect x="400" y="12" width="12" height="12" fill="none" stroke="#fff" stroke-width="2"/>
    <rect x="420" y="12" width="12" height="12" fill="none" stroke="#fff" stroke-width="2"/>
  </svg>
</div>

<section class="abs solutions"></section>
<h2 class="abs heading section-title solutions-title">Our Solutions</h2>
<div class="abs solution" style="left:108px">
  <div class="solution-icon"><svg width="60" height="60" viewBox="0 0 60 60"><path d="M30 8 C40 20 40 36 30 48 C20 36 20 20 30 8Z M30 48 C18 46 8 38 6 26 C18 28 26 36 30 48Z M30 48 C42 46 52 38 54 26 C42 28 34 36 30 48Z" fill="#fff"/></svg></div>
  <h3 class="heading">Meditation</h3>
  <p>Neque porro quisquam est, qui dolorem ipsum quia dolor sit amet, consectetur, adipisci velit, sed quia non numquam eius</p>
  <span class="more">Read More</span>
</div>
<div class="abs solution" style="left:449px">
  <div class="solution-icon"><svg width="60" height="60" viewBox="0 0 60 60"><path d="M30 6 C38 18 42 26 42 32 A12 12 0 0 1 18 32 C18 26 22 18 30 6Z" fill="#fff"/><path d="M8 46 C20 40 40 40 52 46 C40 54 20 54 8 46Z" fill="#fff"/></svg></div>
  <h3 class="heading">Mediums</h3>
  <p>Neque porro quisquam est, qui dolorem ipsum quia dolor sit amet, consectetur, adipisci velit, sed quia non numquam eius</p>
  <span class="more">Read More</span>
</div>
<div class="abs solution" style="left:786px">
  <div class="solution-icon"><svg width="60" height="60" viewBox="0 0 60 60"><circle cx="30" cy="24" r="18" fill="#fff"/><rect x="27" y="30" width="6" height="24" fill="#fff"/></svg></div>
  <h3 class="heading">Healers</h3>
  <p>Neque porro quisquam est, qui dolorem ipsum quia dolor sit amet, consectetur, adipisci velit, sed quia non numquam eius</p>
  <span class="more">Read More</span>
</div>

<section class="abs testimonial" role="img" aria-label="Night photo of a harbour bridge and city lights"></section>
<div class="abs avatar-big" role="img" aria-label="Portrait of the reviewer in a green forest"></div>
<p class="abs quote">"Lorem ipsum dolor sit amet, consectetur adipiscing elit, sed do eiusmod tempor incididunt ut labore et dolore magna aliqua. Ut enim ad minim veniam, quis nostrud exercitation ullamco laboris nisi ut aliquip ex ea commodo consequat."</p>
<p class="abs quote-name">John Doe</p>
<div class="abs dots quote-dots"><span></span><span class="on" style="background:var(--lime)"></span><span></span></div>

<h2 class="abs heading section-title speakers-title">Our <em>Speakers</em></h2>
<article class="abs speaker" style="left:133px">
  <div class="speaker-photo" role="img" aria-label="Portrait of Maren Holloway" style="background:linear-gradient(135deg,#a0603e,#e2b79a)"></div>
  <h3 class="heading">Maren Holloway</h3>
  <p>Everyone is searching for love, joy and peace – aren't we? Yet love, joy and peacels</p>
  <span class="more">Read More »</span>
</article>
<article class="abs speaker" style="left:374px">
  <div class="speaker-photo" role="img" aria-label="Portrait of Ivy Caldwell" style="background:linear-gradient(135deg,#8a5a3a,#e8c9a8)"></div>
  <h3 class="heading">Ivy Caldwell</h3>
  <p>She combines many years of experi-ence in the dental field, with her gentle and friendly</p>
  <span class="more">Read More »</span>
</article>
<article class="abs speaker" style="left:614px">
  <div class="speaker-photo" role="img" aria-label="Portrait of Owen Hartley" style="background:linear-gradient(135deg,#4f77a8,#d7b39a)"></div>
  <h3 class="heading">Owen Hartley</h3>
  <p>She combines many years of experi-ence in the dental field, with her gentle and friendly</p>
  <span class="more">Read More »</span>
</article>
<article class="abs speaker" style="left:851px">
  <div class="speaker-photo" role="img" aria-label="Portrait of Della Prescott" style="background:linear-gradient(135deg,#6e8a5a,#cfae8e)"></div>
  <h3 class="heading">Della Prescott</h3>
  <p>She combines many years of experi-ence in the dental field, with her gentle and friendly</p>
  <span class="more">Read More »</span>
</article>

<section class="abs news"></section>
<h2 class="abs heading section-title news-title">Recent <em>News</em></h2>
<article class="abs post" style="left:133px">
  <div class="post-photo" role="img" aria-label="Woman meditating outdoors in warm sunlight" style="background:linear-gradient(135deg,#6b7a2a,#d8c46a,#8a9a3a)"></div>
  <h3 class="heading">Lorem Ipsum Dolor</h3>
  <time>May05,2016</time>
  <p>Neque porro quisquam est, qui dolorem ipsum quia dolor sit amet, consectetur, adipisci velit, sed quia non numquam eius modi tempora</p>
  <span class="more">Read More »</span>
</article>
<article class="abs post" style="left:455px">
  <div class="post-photo" role="img" aria-label="Woman stretching in a bright sunlit field" style="background:linear-gradient(135deg,#f5f2c0,#cfe6a0,#8fcfc0)"></div>
  <h3 class="heading">Lorem Ipsum Dolor</h3>
  <time>May05,2016</time>
  <p>Neque porro quisquam est, qui dolorem ipsum quia dolor sit amet, consectetur, adipisci velit, sed quia non numquam eius modi tempora</p>
  <span class="more">Read More »</span>
</article>
<article class="abs post" style="left:777px">
  <div class="post-photo" role="img" aria-label="Woman meditating under a pale blue sky" style="background:linear-gradient(135deg,#9fd4e6,#e6f2f4,#7fb86a)"></div>
  <h3 class="heading">Lorem Ipsum Dolor</h3>
  <time>May05,2016</time>
  <p>Neque porro quisquam est, qui dolorem ipsum quia dolor sit amet, consectetur, adipisci velit, sed quia non numquam eius modi tempora</p>
  <span class="more">Read More »</span>
</article>

<footer class="abs site-footer"></footer>
<div class="abs foot-col" style="left:133px">
  <h4>Quick Links</h4>
  <ul class="foot-links"><li>Home</li><li>Our Solution</li><li>Why Choos us?</li><li>About Us</li><li>Blog</li><li>Contact us</li></ul>
</div>
<div class="abs foot-col" style="left:348px">
  <h4>Contact Us</h4>
  <ul class="contact">
    <li><svg width="12" height="12" viewBox="0 0 12 12"><rect width="12" height="12" rx="2" fill="#fff"/><path d="M3 3 C3 7 5 9 9 9 L9 7.5 L7.5 7 L6.8 7.7 C5.6 7.1 4.9 6.4 4.3 5.2 L5 4.5 L4.5 3Z" fill="#333"/></svg><span>(888) 555-0142</span></li>
    <li><svg width="12" height="12" viewBox="0 0 12 12"><rect x="2" y="0" width="8" height="4" fill="#fff"/><rect x="0" y="4" width="12" height="5" fill="#fff"/><rect x="2" y="8" width="8" height="4" fill="#fff"/></svg><span>(888) 555-0187</span></li>
    <li><svg width="12" height="10" viewBox="0 0 12 10"><rect width="12" height="10" fill="#fff"/><path d="M0 0 L6 5 L12 0" fill="none" stroke="#333"/></svg><span style="text-decoration:underline">info@stillmeadowmail.com</span></li>
    <li><svg width="12" height="14" viewBox="0 0 12 14"><path d="M6 0 A6 6 0 0 1 12 6 C12 10 6 14 6 14 C6 14 0 10 0 6 A6 6 0 0 1 6 0Z" fill="#fff"/><circle cx="6" cy="6" r="2" fill="#333"/></svg><span>#2868 Lorem ipsum dolor sit amet,<br>consectetur adipiscing elit</span></li>
  </ul>
</div>
<div class="abs foot-col foot-news" style="left:605px">
  <h4>Newsletter</h4>
  <p>Sign Up for Our Newsletter &amp; Promotion</p>
  <div class="foot-input">Enter Your email Id</div>
  <div class="foot-btn">Subscribe</div>
</div>
<div class="abs foot-brand"><span class="brand-dot"></span><span class="brand-name heading">Still Meadow</span></div>
<div class="abs socials"><span></span><span></span><span></span><span></span></div>
<div class="abs copyright">© 2016 Still Meadow.  All Rights Reserved</div>

</body>
</html>
```